依頼詳細
■ デザイン

期間限定のキャンペーンメニュー(縦)です。

印刷掲示・印刷物配布・HPで使用します。

ファスティング(断食)をするためのリゾートホテルの宿泊客へむけたキャンペーンです。

テーマは、健康、デトックス、ダイエット、美しくなる

メインターゲットは、健康志向が高い女性、30歳~60歳

文字は大きく(50歳代が裸眼で見えるサイズ)

■使用する場所
ホテル内フロント・アロマルームで印刷物にラミネートをかけて掲示します
客室インフォメーションブックで印刷物を掲示します
HPに掲載します

■ 納品ファイル
JPG ai PDF

■添付ファイル
キャンペーン企画書
イメージ画像(必ずしも本画像が必須というわけではありません。お手持ちなどがありましたらご提案ください。)

■デザイン納期
4月上旬予定

■画像
お手持ちのものなど、無償使用できる画像でご提案ください。
場合により弊社所有の画像への入れ替えを提案することがあります。

■最下段には、2パターン店舗情報を記入してください。

■詳しくは企画書をご覧ください。ご不明点はメールでお問い合わせください

記載項目
サイズ
A4
ページ数
片面
希望イメージ
シンプル 複雑
単色 カラフル
暗い 明るい
日常 高級
遊び心 厳粛
未来的 伝統的
女性的 男性的
納品ファイル
• 高解像度JPG (.jpg)
• イラストレーター形式 (.ai)
■ 選んだ理由

本キャンペーンのイメージと、メニューの両方がとてもわかりやすく表現されていました。
1、2つのメニューの見やすい色と配置。
2、年齢層高い方にも文字サイズがほどよい。
3、本企画のテーマが表現されている。
4、季節感が感じられる。
5、シンプルななかにも柑橘が香り立つように盛り込まれている。
などが決め手となりました。

■ 提案者全員のお礼・コメント

この度は弊社コンペに多数ご応募くださいましてありがとうございました。とても素晴らしい作品が多く選出にはとても苦労をしました。また引き続きよろしくお願いいたします。

```html
<!DOCTYPE html>
<html lang="ja">
<head>
<meta charset="utf-8">
<title>爽健アロマデトックス</title>
<link rel="stylesheet" href="https://fonts.googleapis.com/css2?family=Noto+Sans+JP:wght@400;500;700;900&family=Noto+Serif+JP:wght@500;700;900&family=Great+Vibes&display=swap">
<style>
  :root {
    --green: #4f9c3a;
    --green-deep: #2f7a2a;
    --green-pale: #dcefd2;
    --sky: #eaf4f7;
    --sky-deep: #cfe6ee;
    --ink: #3c3a33;
    --brown: #5a4630;
    --orange: #e88a1d;
    --badge: #9a6a3a;
    --row: rgba(255,255,255,0.85);
    --row-alt: rgba(232,244,226,0.85);
  }
  * { margin: 0; padding: 0; box-sizing: border-box; }
  html, body { width: 849px; height: 1200px; overflow: hidden; }
  body {
    position: relative;
    font-family: "Noto Sans JP", sans-serif;
    color: var(--ink);
    background: linear-gradient(180deg, #f7fbfc 0%, var(--sky) 45%, #f3f9f7 75%, #ffffff 100%);
  }
  .photo-treatment {
    position: absolute; left: 200px; top: 120px; width: 649px; height: 480px;
    background: radial-gradient(ellipse at 60% 50%, #f1d6c4 0%, #e9c9b3 25%, #dfe9ec 60%, rgba(234,244,247,0) 80%);
  }
  .photo-citrus {
    position: absolute; right: 0; top: 0; width: 300px; height: 180px;
    background: radial-gradient(circle at 65% 35%, #ffe27a 0%, #f7c843 35%, #f6e7a6 60%, rgba(247,251,252,0) 80%);
  }
  .leaves {
    position: absolute; left: 0; top: 250px; width: 150px; height: 320px;
    background: radial-gradient(ellipse at 20% 50%, #9fd07a 0%, #c9e7b1 40%, rgba(234,244,247,0) 75%);
  }
  .title {
    position: absolute; left: 0; right: 0; top: 28px; text-align: center;
    font-weight: 900; font-size: 70px; letter-spacing: 2px; color: var(--green);
  }
  .title-script {
    position: absolute; left: 300px; top: 78px;
    font-family: "Great Vibes", cursive; font-size: 64px; color: rgba(255,255,255,0.8);
  }
  .intro {
    position: absolute; left: 100px; top: 140px; width: 380px;
    font-size: 16px; line-height: 1.7; font-weight: 500; color: var(--ink);
  }
  .badge {
    position: absolute; left: 615px; top: 385px; width: 180px; height: 180px;
    border-radius: 50%; background: rgba(255,255,255,0.92);
    text-align: center; padding-top: 30px;
  }
  .badge-lead { font-size: 14px; color: var(--green-deep); font-weight: 700; }
  .badge-amount {
    display: inline-block; margin-top: 6px; padding: 2px 14px;
    background: var(--badge); color: #fff; font-weight: 900; font-size: 34px; line-height: 1.2;
  }
  .badge-off {
    display: block; margin: 0 auto; width: 90px;
    background: var(--orange); color: #fff; font-weight: 900; font-size: 28px; line-height: 1.25;
  }
  .badge-note { font-size: 10px; margin-top: 4px; color: var(--ink); }
  .lineart-figure {
    position: absolute; left: 770px; top: 450px; width: 79px; height: 150px;
    background: linear-gradient(180deg, rgba(255,255,255,0.6), rgba(234,244,247,0));
  }
  .citrus-slice {
    position: absolute; left: 0; top: 660px; width: 100px; height: 160px;
    background: radial-gradient(circle at 30% 50%, #ffd36a 0%, #f6a93a 40%, rgba(246,169,58,0) 72%);
  }
  .menu { position: absolute; top: 585px; }
  .menu--diuretic { left: 45px; width: 385px; }
  .menu--refresh { left: 445px; width: 380px; }
  .menu-heading {
    font-family: "Noto Serif JP", serif; color: var(--brown);
    border-bottom: 2px solid var(--brown); padding-bottom: 4px;
    white-space: nowrap;
  }
  .menu-heading .kanji { font-size: 46px; font-weight: 900; }
  .menu-heading .name { font-size: 30px; font-weight: 700; }
  .menu-lead { font-size: 16px; line-height: 1.55; margin-top: 8px; font-weight: 500; }
  .price-table {
    margin-top: 10px; margin-left: 65px; width: 310px; border-collapse: collapse;
  }
  .menu--refresh .price-table { margin-left: 30px; }
  .price-table th {
    background: var(--green); color: #fff; font-size: 16px; font-weight: 700; padding: 4px 0;
  }
  .price-table td {
    font-size: 30px; font-weight: 500; padding: 2px 14px; line-height: 1.35;
    background: var(--row);
  }
  .price-table tr:nth-child(even) td { background: var(--row-alt); }
  .price-table td.course { text-align: left; width: 42%; }
  .price-table td.price { text-align: right; }
  .trial { display: block; font-size: 12px; line-height: 1; padding-top: 3px; color: var(--green-deep); }
  .menu-note {
    font-size: 14px; line-height: 1.55; margin-top: 14px; padding-left: 65px; width: 385px;
  }
  .menu--refresh .menu-note { padding-left: 30px; width: 360px; }
  .inquiry {
    position: absolute; left: 0; right: 0; top: 1108px; text-align: center;
    font-size: 24px; font-weight: 700; color: var(--ink);
  }
  .hours {
    position: absolute; left: 0; right: 0; top: 1152px; height: 38px;
    background: var(--green); color: #fff; text-align: center;
    font-size: 14px; line-height: 38px; font-weight: 500; white-space: nowrap;
  }
</style>
</head>
<body>
  <div class="photo-citrus" role="img" aria-label="グレープフルーツと柑橘の写真"></div>
  <div class="photo-treatment" role="img" aria-label="アロマトリートメントを受けてくつろぐ女性の写真"></div>
  <div class="leaves" role="img" aria-label="みずみずしい緑の葉"></div>

  <h1 class="title">爽健アロマデトックス</h1>
  <div class="title-script">Aroma detox</div>

  <p class="intro">伊豆特産ダイダイとグレープフルーツオイルで、<br>滞った源泉を分解して、リンパ活性トリートメ<br>ントでデトックスをうながします。</p>

  <div class="badge">
    <p class="badge-lead">明日までのご予約で</p>
    <span class="badge-amount">500円</span>
    <span class="badge-off">割引</span>
    <p class="badge-note">※60分以上が対象です</p>
  </div>
  <div class="lineart-figure" role="img" aria-label="線画の女性イラスト"></div>

  <div class="citrus-slice" role="img" aria-label="輪切りのダイダイ"></div>

  <section class="menu menu--diuretic">
    <h2 class="menu-heading"><span class="kanji">利尿</span> <span class="name">デトックスボディ</span></h2>
    <p class="menu-lead">むくみや冷え性を軽くするために、<br>余分な水分の排出をサポートします</p>
    <table class="price-table">
      <tr><th>コース</th><th>価格</th></tr>
      <tr><td class="course"><span class="trial">おためし</span>45分</td><td class="price">6,300円</td></tr>
      <tr><td class="course">60分</td><td class="price">8,470円</td></tr>
      <tr><td class="course">90分</td><td class="price">12,540円</td></tr>
      <tr><td class="course">120分</td><td class="price">15,730円</td></tr>
    </table>
    <p class="menu-note">グレープフルーツオイルに含まれるD-リモネン成分が、余分な水分の排出をうながし、香り高い柑橘がむくみ知らずのボディをサポートします。</p>
  </section>

  <section class="menu menu--refresh">
    <h2 class="menu-heading"><span class="kanji">爽快</span> <span class="name">デトックスボディ</span></h2>
    <p class="menu-lead">腸を活性化することで、<br>老廃物の排出力を高めます</p>
    <table class="price-table">
      <tr><th>コース</th><th>価格</th></tr>
      <tr><td class="course"><span class="trial">おためし</span>45分</td><td class="price">6,300円</td></tr>
      <tr><td class="course">60分</td><td class="price">8,470円</td></tr>
      <tr><td class="course">90分</td><td class="price">12,540円</td></tr>
      <tr><td class="course">120分</td><td class="price">15,730円</td></tr>
    </table>
    <p class="menu-note">伊豆ダイダイが副交感神経を刺激して大腸を活性化。ペパーミントやジンジャー成分で腸の動きを高めデトックスをサポートします。</p>
  </section>

  <p class="inquiry">お問合せはフロントで承ります</p>
  <p class="hours">営業時間 15:00～22:00　受付時間 15:00～18:00　アロマルーム（東館）1階にございます（全コース男女とも施術可能です）</p>
</body>
</html>
```